we need a homepage for a marketplace

We manage all projects using our ground-breaking platform Kelvrim Hub. You get access to 150+ partners in 70 countries, security, cost efficiency, technical skills, speed, 100% visibility and accountability.Kelvrim aims to help clients realize the full potential of their investments, provide a competitive price, establish the business need as a competitive advantage, and provide a strategic business asset that can facilitate growth.
Target Market(s)
Freelancers
Industry/Entity Type
Business Software
Number of Pages Required
1 page
Requirements
Must have
- Credentials -http://qabdel.example/freelancer/public
- Front :
- Client:
- Email id - tomasp@lurvantsystems.example
- Password - 908172
- Partner:
- Email id - dorian@lurvantsystems.example
- Password - 908172
- Project Manager:
- Email id - mirela@lurvantsystems.example
- Password - 908172
Nice to have
- It will be nice to have a creative design, and a outside the box look/feel

```html
<!DOCTYPE html>
<html lang="en">
<head>
<meta charset="utf-8">
<title>Kelvrim Hub — Sign In</title>
<link href="https://fonts.googleapis.com/css2?family=Nunito+Sans:wght@700;800&family=Questrial&display=swap" rel="stylesheet">
<style>
  :root {
    --night: #0a0e1a;
    --night-mid: #111a30;
    --night-deep: #0c1324;
    --field: rgba(120, 124, 140, 0.32);
    --accent: #1363ee;
    --white: #ffffff;
    --footer: #232323;
    --footer-text: #e6e6e6;
  }
  * { box-sizing: border-box; margin: 0; padding: 0; }
  html, body { width: 1200px; height: 800px; overflow: hidden; background: var(--night); }
  .page { position: relative; width: 1200px; height: 800px; font-family: "Nunito Sans", sans-serif; color: var(--white); }

  .hero-backdrop {
    position: absolute; left: 0; top: 0; width: 1200px; height: 674px;
    background:
      radial-gradient(ellipse 420px 520px at 330px 420px, rgba(40, 58, 96, 0.45), transparent 70%),
      radial-gradient(ellipse 380px 560px at 1000px 300px, rgba(44, 60, 98, 0.4), transparent 70%),
      linear-gradient(180deg, var(--night) 0%, var(--night-deep) 40%, var(--night-mid) 100%);
  }

  .auth { position: absolute; left: 440px; top: 240px; width: 320px; }
  .auth-tabs { position: relative; height: 30px; }
  .auth-tab { position: absolute; top: 0; font-size: 16px; font-weight: 800; letter-spacing: 0.8px; line-height: 26px; color: var(--white); text-decoration: none; }
  .auth-tab--active { left: 1px; padding: 0 2px; border-bottom: 2px solid var(--accent); }
  .auth-tab--signup { right: 2px; }

  .field-label { position: absolute; left: 1px; font-size: 11px; font-weight: 800; letter-spacing: 0.4px; }
  .field-label--user { top: 67px; }
  .field-label--pass { top: 156px; }
  .field-input { position: absolute; left: 0; width: 320px; height: 36px; border: 0; background: var(--field); color: var(--white); padding: 0 12px; font: inherit; font-size: 14px; outline: none; }
  .field-input--user { top: 88px; }
  .field-input--pass { top: 176px; }
  .help-button { position: absolute; left: 287px; top: 180px; width: 28px; height: 28px; background: var(--accent); color: var(--white); font-size: 18px; font-weight: 800; line-height: 28px; text-align: center; }

  .submit { position: absolute; left: 0; top: 264px; width: 320px; height: 36px; border: 0; background: var(--accent); color: var(--white); font-family: inherit; font-size: 16px; font-weight: 800; letter-spacing: 1px; }

  .site-footer { position: absolute; left: 0; top: 674px; width: 1200px; height: 126px; background: var(--footer); font-family: "Questrial", sans-serif; font-size: 15px; color: var(--footer-text); }
  .copyright { position: absolute; left: 82px; top: 53px; }
  .copyright strong { font-family: "Nunito Sans", sans-serif; font-weight: 800; color: var(--white); }
  .footer-nav { position: absolute; left: 666px; top: 53px; display: flex; align-items: center; }
  .footer-nav a { color: var(--footer-text); text-decoration: none; }
  .footer-dot { display: inline-block; width: 8px; height: 8px; background: var(--accent); margin: 2px 37px 0; }
</style>
</head>
<body>
<div class="page">
  <div class="hero-backdrop" role="img" aria-label="Dark blue upward view of glass skyscrapers"></div>

  <form class="auth">
    <div class="auth-tabs">
      <a class="auth-tab auth-tab--active" href="#">SIGN IN</a>
      <a class="auth-tab auth-tab--signup" href="#">SIGN UP</a>
    </div>
    <label class="field-label field-label--user" for="username">USERNAME</label>
    <input class="field-input field-input--user" id="username" type="text">
    <label class="field-label field-label--pass" for="password">PASSWORD</label>
    <input class="field-input field-input--pass" id="password" type="password">
    <span class="help-button">?</span>
    <button class="submit" type="submit">SIGN IN</button>
  </form>

  <footer class="site-footer">
    <p class="copyright">Copyright 2016 <strong>KELVRIM</strong>. ALL Rights Reserved.</p>
    <nav class="footer-nav">
      <a href="#">Privacy Policy</a><span class="footer-dot"></span>
      <a href="#">Terms &amp; Conditions</a><span class="footer-dot"></span>
      <a href="#">Sitemap</a>
    </nav>
  </footer>
</div>
</body>
</html>
```